Business Card for new Architectural Firm

I intend to practice in a rural mountain community in upstate NY, focusing on residential and light commercial projects, including second home / vacation properties. I wish to convey a feeling of rural outdoorsy modernity.

Color is important - bold and urbane. Secondary or tertiary colors preferred.

Font is important, idiosyncratic is ok

Optionally, I may choose to use the name Brackenfold Studio. If used as part of your design, all of the Must Haves are still required.

Images uploaded are logos I like

Industry/Entity Type

Residential

Contact Information for Business Card

Lionel Harwicke
Architect (This word should stand alone or be associated with my name - not license number)
NY License No. 052816
lionel@designlhq.com
607 382 9154

Font styles to use
Sans Serif
Decorative

Requirements
Must have
• Whatever files I need to best utilize your design
• PDF
• JPG
• EPS
• Vectorwhatsit
Nice to have
• Logo or element that can be incorporated into other print material.
• Could be a font based card
Should not have
• no clip art
• No templates
• no floor plans
• no building photographs

```html
<!DOCTYPE html>
<html lang="en">
<head>
<meta charset="utf-8">
<title>Brackenfold Studio – Lionel Harwicke, Architect</title>
<link href="https://fonts.googleapis.com/css2?family=Source+Sans+3:wght@400;700&family=Yesteryear&display=swap" rel="stylesheet">
<style>
  :root {
    --ink: #141414;
    --slate: #7d848c;
    --muted: #8a8f95;
    --paper: #ffffff;
    --sans: "Source Sans 3", sans-serif;
    --script: "Yesteryear", cursive;
  }
  * { margin: 0; padding: 0; box-sizing: border-box; }
  html, body { width: 927px; height: 1200px; overflow: hidden; background: var(--paper); }
  .sheet { position: relative; width: 927px; height: 1200px; }
  .abs { position: absolute; }

  .wordmark { display: block; overflow: visible; }
  .wordmark text {
    font-family: var(--sans); font-weight: 700; fill: var(--ink);
    text-transform: uppercase;
  }

  .signature { font-family: var(--script); color: var(--ink); text-align: center; line-height: 1; }
  .signature span { display: block; }

  .band { display: block; }

  .contacts { list-style: none; font-family: var(--sans); color: var(--muted); }
  .contacts li { display: flex; align-items: center; }
  .contacts svg { flex: none; fill: none; stroke: var(--muted); }
  .contacts .fill { fill: var(--muted); stroke: none; }
</style>
</head>
<body>
<main class="sheet">

  <!-- Primary wordmark -->
  <svg class="wordmark abs" style="left:158px; top:48px" width="610" height="70" viewBox="0 0 610 70">
    <text x="0" y="60" font-size="66" textLength="610" lengthAdjust="spacingAndGlyphs">Brackenfold Studio</text>
  </svg>

  <!-- Name signature -->
  <div class="signature abs" style="left:180px; top:185px; width:560px; font-size:76px;">
    <span>Lionel Harwicke</span>
    <span style="margin-top:8px">Architect</span>
  </div>

  <!-- Large card -->
  <section class="card-large">
    <svg class="band abs" style="left:175px; top:437px" width="580" height="104" viewBox="0 0 580 104">
      <rect x="0" y="0" width="580" height="9" fill="var(--ink)"/>
      <rect x="0" y="9" width="580" height="86" fill="var(--slate)" role="img" aria-label="Forest of bare tree trunks and branches"/>
      <rect x="0" y="95" width="580" height="9" fill="var(--ink)"/>
    </svg>

    <svg class="wordmark abs" style="left:185px; top:560px" width="557" height="56" viewBox="0 0 557 56">
      <text x="0" y="50" font-size="56" textLength="557" lengthAdjust="spacingAndGlyphs">Brackenfold Studio</text>
    </svg>

    <ul class="contacts abs" style="left:186px; top:640px; font-size:22px;">
      <li style="height:34px">
        <svg width="26" height="26" viewBox="0 0 24 24"><path class="fill" d="M6.6 10.8a15 15 0 0 0 6.6 6.6l2.2-2.2c.3-.3.7-.4 1-.2 1.1.4 2.3.6 3.6.6.6 0 1 .4 1 1V20c0 .6-.4 1-1 1A17 17 0 0 1 3 4c0-.6.4-1 1-1h3.5c.6 0 1 .4 1 1 0 1.3.2 2.5.6 3.6.1.3 0 .7-.2 1z"/></svg>
        <span style="margin-left:12px">607 382 9154</span>
      </li>
      <li style="height:34px; margin-top:12px">
        <svg width="26" height="26" viewBox="0 0 24 24" stroke-width="2.4"><circle cx="12" cy="12" r="9.5"/><path d="M8 16l8-8M9 8l2 2M13 14l2 2"/></svg>
        <span style="margin-left:12px">NY License No. 052816</span>
      </li>
      <li style="height:34px; margin-top:10px">
        <svg width="26" height="26" viewBox="0 0 24 24" stroke-width="1.8"><circle cx="12" cy="12" r="9.5"/><path d="M2.5 12h19M12 2.5c3 3 3 16 0 19M12 2.5c-3 3-3 16 0 19M4.5 7h15M4.5 17h15"/></svg>
        <span style="margin-left:12px">lionel@designlhq.com</span>
      </li>
    </ul>

    <div class="signature abs" style="left:478px; top:668px; width:240px; font-size:36px;">
      <span>Lionel Harwicke</span>
      <span style="margin-top:6px">Architect</span>
    </div>
  </section>

  <!-- Small card -->
  <section class="card-small">
    <svg class="band abs" style="left:263px; top:916px" width="403" height="75" viewBox="0 0 403 75">
      <rect x="0" y="0" width="403" height="6" fill="var(--ink)"/>
      <rect x="0" y="6" width="403" height="63" fill="var(--slate)" role="img" aria-label="Forest of bare tree trunks and branches"/>
      <rect x="0" y="69" width="403" height="6" fill="var(--ink)"/>
    </svg>

    <svg class="wordmark abs" style="left:265px; top:1000px" width="385" height="40" viewBox="0 0 385 40">
      <text x="0" y="36" font-size="40" textLength="385" lengthAdjust="spacingAndGlyphs">Brackenfold Studio</text>
    </svg>

    <ul class="contacts abs" style="left:273px; top:1057px; font-size:15px;">
      <li style="height:24px">
        <svg width="18" height="18" viewBox="0 0 24 24"><path class="fill" d="M6.6 10.8a15 15 0 0 0 6.6 6.6l2.2-2.2c.3-.3.7-.4 1-.2 1.1.4 2.3.6 3.6.6.6 0 1 .4 1 1V20c0 .6-.4 1-1 1A17 17 0 0 1 3 4c0-.6.4-1 1-1h3.5c.6 0 1 .4 1 1 0 1.3.2 2.5.6 3.6.1.3 0 .7-.2 1z"/></svg>
        <span style="margin-left:9px">607 382 9154</span>
      </li>
      <li style="height:24px; margin-top:7px">
        <svg width="18" height="18" viewBox="0 0 24 24" stroke-width="2.4"><circle cx="12" cy="12" r="9.5"/><path d="M8 16l8-8M9 8l2 2M13 14l2 2"/></svg>
        <span style="margin-left:9px">NY License No. 052816</span>
      </li>
      <li style="height:24px; margin-top:7px">
        <svg width="18" height="18" viewBox="0 0 24 24" stroke-width="1.8"><circle cx="12" cy="12" r="9.5"/><path d="M2.5 12h19M12 2.5c3 3 3 16 0 19M12 2.5c-3 3-3 16 0 19M4.5 7h15M4.5 17h15"/></svg>
        <span style="margin-left:9px">lionel@designlhq.com</span>
      </li>
    </ul>

    <div class="signature abs" style="left:478px; top:1066px; width:196px; font-size:28px;">
      <span>Lionel Harwicke</span>
      <span style="margin-top:6px">Architect</span>
    </div>
  </section>

</main>
</body>
</html>
```